Redgum Party Box and Bouncer Hire

Hi folks,
This is for a new business based in Brisbane(Australia), the business hires, jukeboxes, inflatable games(mostly jumping castles) and slushy/cocktail machines.
I want the website to appeal to people looking to party. Does that sound too simplistic?
It should be simple to navigate, I require only the front page but make it easy to get to the rest of the site.
Modern, exciting and funky, think rock band or concert promoter.
We are trying to sell packages of products, there should be several packages visible on the front page without looking cluttered.
Link to jukebox song list.
Facebook, twitter etc.
I am currently on holidays so I have a fair amount of time to get this project done, it says 10 days I hope to have it done much sooner.

Reason: So far there is no design that I am happy with. I am after a website for Jukeboxes, it should have a rock concert feel.

Target Market(s)

Ages 20 to 50

Industry/Entity Type

Business

Requirements
Must have
• Think rock band type website, black with bold color highlight.
Should not have
• Plain or bland color.
Pictures of Brisbane or any other city.
Google map or any other location type map.

```html
<!DOCTYPE html>
<html lang="en">
<head>
<meta charset="utf-8">
<title>Redgum Party Box and Bouncer Hire</title>
<link rel="stylesheet" href="https://fonts.googleapis.com/css2?family=Cabin:ital,wght@0,400;0,500;0,700;1,400&display=swap">
<style>
  :root {
    --bg: #050505;
    --ink: #ffffff;
    --accent: #e0301c;
    --sky: #9fdcf5;
    --gold: #f5c400;
    --gold-light: #fff36a;
    --muted: #3a3a3a;
    --faint: #2b2b2b;
  }
  * { box-sizing: border-box; margin: 0; padding: 0; }
  html, body { width: 900px; height: 1200px; overflow: hidden; background: var(--bg); }
  body {
    position: relative;
    font-family: "Cabin", sans-serif;
    color: var(--ink);
    background:
      radial-gradient(ellipse 520px 90px at 450px 470px, rgba(80,80,80,.35), transparent 70%),
      radial-gradient(ellipse 700px 120px at 300px 640px, rgba(60,60,60,.35), transparent 70%),
      radial-gradient(ellipse 600px 110px at 600px 860px, rgba(55,55,55,.3), transparent 70%),
      var(--bg);
  }
  .hero {
    position: absolute; left: 86px; top: 58px; width: 727px; height: 390px;
    overflow: hidden; border-radius: 2px;
  }
  .hero-photo {
    position: absolute; inset: 0;
    background:
      radial-gradient(ellipse 260px 180px at 370px 170px, rgba(230,245,255,.95), transparent 70%),
      linear-gradient(100deg, #b8312b 0%, #2a6fa8 22%, #5fc0ee 45%, #4fb1e6 60%, #d0771e 82%, #7b2a12 100%);
  }
  .hero-shade {
    position: absolute; left: 0; right: 0; bottom: 0; height: 70px;
    background: linear-gradient(to bottom, transparent, rgba(0,0,0,.75));
  }
  .pill {
    position: absolute; display: flex; align-items: center; justify-content: center; text-align: center;
    border-radius: 50%;
    background: radial-gradient(ellipse at 50% 35%, var(--gold-light), var(--gold) 60%, #d58a00);
    color: #1a1a1a; font-size: 15px; line-height: 1.15;
    box-shadow: 0 0 14px rgba(255,220,80,.55);
  }
  .pill-join { left: 51px; top: 43px; width: 117px; height: 62px; }
  .pill-songs { left: 529px; top: 394px; width: 117px; height: 64px; font-size: 14px; z-index: 2; }
  .hero-title {
    position: absolute; left: 0; right: 0; top: 198px; text-align: center;
    font-size: 18px; color: #111;
  }
  .hero-mark {
    position: absolute; left: 0; right: 0; top: 221px; text-align: center;
    font-weight: 700; font-size: 42px; line-height: 1; color: var(--accent); letter-spacing: 2px;
  }
  .hero-nav {
    position: absolute; left: 0; right: 0; top: 286px; text-align: center;
    font-size: 12.5px; color: #111;
  }
  .hero-nav span { margin: 0 5px; }
  .hero-arrow { position: absolute; top: 180px; width: 30px; height: 40px; }
  .hero-arrow.prev { left: 28px; }
  .hero-arrow.next { right: 22px; }

  .welcome { position: absolute; left: 108px; top: 480px; width: 700px; }
  .welcome h1 { font-style: italic; font-weight: 400; font-size: 20px; color: var(--accent); margin-bottom: 22px; }
  .welcome p { font-size: 13px; line-height: 1.28; margin-bottom: 17px; }
  .welcome p b { color: var(--accent); font-weight: 400; margin-right: 10px; }

  .packs {
    position: absolute; left: 162px; top: 659px;
    display: grid; grid-template-columns: repeat(6, 85px); column-gap: 15px; row-gap: 12px;
  }
  .pack {
    width: 85px; height: 115px; border-radius: 6px; overflow: hidden; background: #fff;
    box-shadow: 0 0 14px rgba(224,48,28,.75);
  }
  .pack-label {
    height: 29px; display: flex; align-items: center; justify-content: center;
    background: linear-gradient(var(--sky), #5fc4ef); color: #111; font-size: 14px;
  }
  .pack-photo { height: 86px; }
  .castle { background: linear-gradient(135deg, #e3262a, #f7d119 45%, #2a64c7 75%, #f2f2f2); }
  .jukebox { background: radial-gradient(ellipse at 50% 30%, #f3a316, #7a2a12 55%, #1b1b1b 90%); }

  .footer-rule { position: absolute; left: 83px; top: 949px; width: 730px; height: 3px; background: #7d1f12; }
  .footer-bg {
    position: absolute; left: 83px; top: 952px; width: 730px; height: 248px;
    background: linear-gradient(to bottom, rgba(70,70,70,.35), rgba(30,30,30,.4));
  }
  .footer-links { position: absolute; left: 83px; top: 996px; list-style: none; font-size: 14px; line-height: 16.5px; }
  .footer-links li::before, .follow::before, .footer-note::before { content: ">"; color: var(--accent); margin-right: 8px; }
  .follow { position: absolute; left: 413px; top: 996px; font-size: 14px; }
  .social { position: absolute; left: 361px; top: 1031px; display: flex; gap: 17px; }
  .social span { width: 31px; height: 31px; border-radius: 4px; background: linear-gradient(#4a4a4a, #1c1c1c); border: 1px solid #555; }
  .footer-note { position: absolute; left: 632px; top: 996px; width: 150px; font-size: 13.5px; line-height: 16.5px; padding-left: 14px; text-indent: -14px; }
  .footer-name { position: absolute; left: 0; right: 0; top: 1075px; text-align: center; font-size: 18px; color: var(--muted); }
  .footer-mark { position: absolute; left: 0; right: 0; top: 1112px; text-align: center; font-weight: 700; font-size: 42px; line-height: 1; letter-spacing: 2px; color: var(--faint); }
  .copyright { position: absolute; left: 0; right: 0; top: 1166px; text-align: center; font-size: 12px; color: #ddd; }
</style>
</head>
<body>
  <section class="hero">
    <div class="hero-photo" role="img" aria-label="Concert stage with lights, a jumping man, an inflatable castle and a jukebox"></div>
    <div class="hero-shade"></div>
    <div class="pill pill-join">JOIN<br>NOW!</div>
    <p class="hero-title">Redgum Party Box and Bouncer Hire</p>
    <p class="hero-mark">REDGUM</p>
    <nav class="hero-nav">HOME<span>|</span>ABOUT US<span>|</span>CONTACT<span>|</span>GALLERY</nav>
    <svg class="hero-arrow prev" viewBox="0 0 30 40"><path d="M22 4 L8 20 L22 36" fill="none" stroke="#fff" stroke-width="6"/></svg>
    <svg class="hero-arrow next" viewBox="0 0 30 40"><path d="M8 4 L22 20 L8 36" fill="none" stroke="#fff" stroke-width="6"/></svg>
  </section>
  <div class="pill pill-songs">Jukebox<br>Song list</div>

  <section class="welcome">
    <h1>Welcome to our site!</h1>
    <p><b>&gt;</b>Lorem ipsum dolor sit amet, consectetur adipisicing elit, sed do eiusmod tempor incididunt ut labore et dolore magna. Ut enim ad minim veniam, quis nostrud exercitation ullamco laboris nisi ut aliquip ex ea commodo consequat.</p>
    <p><b>&gt;</b>Duis aute irure dolor in reprehenderit in voluptate velit esse cillum dolore eu fugiat nulla pariatur. Excepteur sint occae cupidatat non proident, sunt in culpa qui officia deserunt mollit anim id est laborum.</p>
  </section>

  <section class="packs">
    <div class="pack"><div class="pack-label">PACK 1</div><div class="pack-photo castle" role="img" aria-label="Inflatable jumping castle"></div></div>
    <div class="pack"><div class="pack-label">PACK 2</div><div class="pack-photo castle" role="img" aria-label="Inflatable play pen"></div></div>
    <div class="pack"><div class="pack-label">PACK 3</div><div class="pack-photo castle" role="img" aria-label="Inflatable obstacle course"></div></div>
    <div class="pack"><div class="pack-label">PACK 4</div><div class="pack-photo jukebox" role="img" aria-label="Jukebox"></div></div>
    <div class="pack"><div class="pack-label">PACK 5</div><div class="pack-photo jukebox" role="img" aria-label="Wooden jukebox"></div></div>
    <div class="pack"><div class="pack-label">PACK 6</div><div class="pack-photo jukebox" role="img" aria-label="Neon jukebox"></div></div>
    <div class="pack"><div class="pack-label">PACK 1</div><div class="pack-photo castle" role="img" aria-label="Inflatable jumping castle"></div></div>
    <div class="pack"><div class="pack-label">PACK 2</div><div class="pack-photo castle" role="img" aria-label="Inflatable play pen"></div></div>
    <div class="pack"><div class="pack-label">PACK 3</div><div class="pack-photo castle" role="img" aria-label="Inflatable obstacle course"></div></div>
    <div class="pack"><div class="pack-label">PACK 4</div><div class="pack-photo jukebox" role="img" aria-label="Jukebox"></div></div>
    <div class="pack"><div class="pack-label">PACK 5</div><div class="pack-photo jukebox" role="img" aria-label="Wooden jukebox"></div></div>
    <div class="pack"><div class="pack-label">PACK 6</div><div class="pack-photo jukebox" role="img" aria-label="Neon jukebox"></div></div>
  </section>

  <footer>
    <div class="footer-rule"></div>
    <div class="footer-bg" role="img" aria-label="Faded concert stage scene"></div>
    <ul class="footer-links">
      <li>HOME</li>
      <li>ABOUT US</li>
      <li>GALLERY PHOTOS</li>
      <li>GALLERY VIDEOS</li>
      <li>NEWS</li>
    </ul>
    <p class="follow">Folow us</p>
    <div class="social" aria-label="Social links"><span></span><span></span><span></span><span></span></div>
    <p class="footer-note">Lorem ipsum dolor sit amet, consectetur adipisicing elit, sed do eiusmod tempor incidi.</p>
    <p class="footer-name">Redgum Party Box and Bouncer Hire</p>
    <p class="footer-mark">REDGUM</p>
    <p class="copyright">Copyright 2014 | All Rights Reserved</p>
  </footer>
</body>
</html>
```